SEO Company Needs a Professional, Bold Business Card Design

Kelvo SEO
2487 N Harlow Ave #315
Dunmore, TX 75990
512-555-0184
http://www.kelvoseo-demo.com
Kelvo SEO is an internet marketing company specializing in SEO for higher-end businesses. We are looking for a professional and bold (edgy) design that communicates our forward thinking SEO strategies. Our typical client is a small to medium US business that has never had SEO work done on their website but does has active marketing. We want our business card design to instill confidence in our services through a professional and bold look. We we would also like the design elements to be in line with the services we offer - ranking client websites in the search engine results, namely Zarnix.
Design Specifics:
Card design should have square edges.
Design should be delivered in fully layered and editable PSD file. Designing in AI is fine but I need a PSD file in case we have any changes in contact information or need additional cards for employees.
The design should compliment the attached logo.
Company Name:
Kelvo SEO
Address:
2487 N Harlow Ave #315
Dunmore, TX 75990
Personal Info:
Dorian Welk
Owner
hello@kelvoseo-demo.com
Phone:
877-555-0139 (KELVO UP)
Website:
http://www.kelvoseo-demo.com
Slogan:
Could Your Website Be Generating More Business?
Target Market(s)
High-end business owners - doctors, lawyers, specialists, business owners doing 250k in profit.
Industry/Entity Type
Internet
Contact Information for Business Card
Company Name:
Kelvo SEO
Address:
480 Larkin Ridge Ste 210
Dunmore, TX 75990
Personal Info:
Dorian Welk
Owner
hello@kelvoseo-demo.com
Phone:
877-555-0139 (KELVO UP)
Website:
www.kelvoseo-demo.com
Slogan:
Requirements
Must have
- Card design should have square edges.
- Background should be WHITE only.
- Design should be delivered in fully layered and editable PSD file. Designing in AI is fine but I need a PSD file in case we have any changes in contact information or need additional cards for employees.

```html
<!DOCTYPE html>
<html lang="en">
<head>
<meta charset="utf-8">
<title>Kelvo SEO – Business Card</title>
<link href="https://fonts.googleapis.com/css2?family=Exo+2:ital,wght@0,400;0,500;0,700;0,800;1,400&display=swap" rel="stylesheet">
<style>
  :root{
    --bg:#e9e9e6;
    --card:#ffffff;
    --navy:#1d3a5c;
    --ink:#233246;
    --sky:#3aa8dc;
    --icon:#4fb1e0;
    --muted:#4b5a6e;
  }
  *{margin:0;padding:0;box-sizing:border-box}
  html,body{width:1200px;height:885px;overflow:hidden;background:var(--bg)}
  body{position:relative;font-family:"Exo 2",sans-serif;color:var(--ink)}
  .card{position:absolute;width:560px;height:320px;background:var(--card);
    box-shadow:0 2px 6px rgba(0,0,0,.12)}
  .card--front{left:50px;top:110px}
  .card--back{left:590px;top:455px}

  /* front */
  .address{position:absolute;right:34px;top:30px;text-align:right;font-size:17px;line-height:1.3;color:var(--muted)}
  .brand{position:absolute;display:flex;align-items:center;gap:10px;font-weight:800;color:var(--navy);white-space:nowrap}
  .card--front .brand{right:40px;top:135px;font-size:40px}
  .brand-dot{display:block;border-radius:50%;background:var(--navy)}
  .card--front .brand-dot{width:34px;height:34px}
  .person{position:absolute;left:34px;bottom:30px}
  .person-name{font-weight:800;font-size:22px;letter-spacing:.5px;color:var(--navy);text-transform:uppercase}
  .person-role{font-size:18px;color:var(--sky);margin-bottom:14px}
  .contact-line{display:flex;align-items:center;gap:10px;font-size:15px;color:var(--ink);height:22px;white-space:nowrap}
  .contact-icon{width:18px;height:18px;flex:none}

  /* back */
  .card--back .brand{left:0;right:0;top:100px;justify-content:center;font-size:64px}
  .card--back .brand-dot{width:52px;height:52px}
  .slogan{position:absolute;left:0;right:0;top:205px;text-align:center;font-style:italic;font-size:19px;color:var(--navy)}
</style>
</head>
<body>
  <section class="card card--front" aria-label="Business card front">
    <div class="address">480 Larkin Ridge Ste 210<br>Dunmore, TX 75990</div>
    <div class="brand"><span class="brand-dot"></span>Kelvo SEO</div>
    <div class="person">
      <div class="person-name">Dorian Welk</div>
      <div class="person-role">Owner</div>
      <div class="contact-line">
        <svg class="contact-icon" viewBox="0 0 18 18" aria-hidden="true"><rect width="18" height="18" fill="var(--icon)"/><path d="M5 4h2.5l1 3-1.5 1a6 6 0 0 0 3 3l1-1.5 3 1V13a1 1 0 0 1-1 1A9 9 0 0 1 4 5a1 1 0 0 1 1-1z" fill="#fff"/></svg>
        <span>877-555-0139 (KELVO UP)</span>
      </div>
      <div class="contact-line">
        <svg class="contact-icon" viewBox="0 0 18 18" aria-hidden="true"><rect width="18" height="18" fill="var(--icon)"/><rect x="3.5" y="5" width="11" height="8" fill="none" stroke="#fff" stroke-width="1.4"/><path d="M3.5 5 9 9.5 14.5 5" fill="none" stroke="#fff" stroke-width="1.4"/></svg>
        <span>hello@kelvoseo-demo.com</span>
      </div>
      <div class="contact-line">
        <svg class="contact-icon" viewBox="0 0 18 18" aria-hidden="true"><rect width="18" height="18" fill="var(--icon)"/><g fill="none" stroke="#fff" stroke-width="1.2"><circle cx="9" cy="9" r="5.5"/><ellipse cx="9" cy="9" rx="2.4" ry="5.5"/><path d="M3.5 9h11"/></g></svg>
        <span>www.kelvoseo-demo.com</span>
      </div>
    </div>
  </section>

  <section class="card card--back" aria-label="Business card back">
    <div class="brand"><span class="brand-dot"></span>Kelvo SEO</div>
    <p class="slogan">Could Your Website Be Generating More Business?</p>
  </section>
</body>
</html>
```